1 Page Sales Brochure of our Services

I need to create a one page brochure that our sales team can take into meetings about our services - Need this to be an impressive one page that looks fresh and new using our brand colors of Vantora green, black and white. Our brand looks "clean" think Quenly brand in how everything is clean and white and crisp. Our website showcases our services: https://vantorasports.com/services/ --- After done with this project I would like to create a full booklet. Want to begin with this project first.

Target Market(s)

State of Texas

Industry/Entity Type

Sports Construction in Texas Only

Font styles to use
Serif

Colors
00AB8E
00BBA5
67D7C9
C6EFE9
E9F9F6

Requirements
Must have
• Front and Back and cover our services outlined on our website: https://vantorasports.com/services/
Nice to have
• Need one that can get sent digital and printed -- Our colors are the Vantora green, white and black - We want brochure to look clean, almost like the Quenly feel of their product's branding

```html
<!DOCTYPE html>
<html lang="en">
<head>
<meta charset="utf-8">
<title>Vantora Sports Construction – Services Brochure</title>
<link href="https://fonts.googleapis.com/css2?family=Oswald:wght@300;400&family=Source+Sans+3:wght@400;600&display=swap" rel="stylesheet">
<style>
:root{
  --green:#17703a;
  --green-dark:#0f5a2d;
  --ink:#2b2b2b;
  --text:#444;
  --footer-dark:#333333;
  --paper:#ffffff;
  --stage:#e4e4e4;
  --rule:#1f7a42;
}
*{box-sizing:border-box;margin:0;padding:0}
html,body{width:1200px;height:791px;overflow:hidden;background:var(--stage);font-family:"Source Sans 3",sans-serif;color:var(--text)}
.sheet{position:absolute;top:86px;width:490px;height:633px;background:var(--paper);overflow:hidden;box-shadow:0 2px 6px rgba(0,0,0,.25)}
.sheet--front{left:90px}
.sheet--back{left:623px}
.abs{position:absolute}
.heading{font-family:"Oswald",sans-serif;font-weight:300;color:var(--ink);text-transform:uppercase;line-height:1;white-space:nowrap}
.photo{position:absolute}
.rule{position:absolute;height:1px;background:var(--rule)}
.body{font-size:8.4px;line-height:11.2px;text-align:justify}

/* front */
.brand{left:24px;top:16px}
.brand__name{font-family:"Oswald",sans-serif;font-weight:300;font-size:34px;color:var(--green);line-height:1}
.brand__sub{font-size:8.5px;color:var(--ink);margin-left:44px;margin-top:1px;letter-spacing:.3px}
.tagline{left:258px;top:35px;font-size:14px;transform:scaleX(.86);transform-origin:left}
.hero-front{left:0;top:69px;width:490px;height:207px;background:linear-gradient(160deg,#8a8c78 0%,#b7b0a2 35%,#c9c4bb 60%,#8e9190 100%)}
.services-title{left:22px;top:312px;font-size:20px}
.services-copy{left:22px;top:346px;width:223px}
.services-copy p+p{margin-top:11px}
.include-box{left:276px;top:295px;width:214px;height:181px;background:var(--green);border-top-left-radius:6px;padding:18px 12px 0 12px;color:#fff}
.include-box .heading{color:#fff;font-size:19px}
.include-box__rule{height:1px;background:rgba(255,255,255,.6);width:48px;margin:6px 0 8px -12px}
.service-list{list-style:none}
.service-list li{font-size:9.6px;line-height:16px;display:flex;align-items:center;gap:7px}
.service-list svg{width:7px;height:6px}
.gallery{top:489px;width:136px;height:88px}
.gallery-caption{top:582px;width:136px;text-align:center;font-size:6.6px;color:var(--ink);text-transform:uppercase;letter-spacing:-.1px}

/* footer */
.footer{position:absolute;left:0;bottom:0;width:490px;height:32px}
.footer svg{position:absolute;inset:0}
.footer__web{position:absolute;left:24px;top:9px;color:#fff;font-size:11.5px;display:flex;align-items:center;gap:4px}
.footer__web i{width:6px;height:6px;border:1.2px solid #fff;border-radius:50%;display:block}
.footer__contact{position:absolute;left:182px;top:12px;color:#fff;font-size:6px;white-space:nowrap;letter-spacing:-.1px}

/* back */
.hero-back{left:0;top:0;width:490px;height:204px;background:linear-gradient(170deg,#7f8c80 0%,#a9b2b4 30%,#3f7d3c 55%,#9e8d80 75%,#c5c9c8 100%)}
.thumb{left:16px;width:132px;height:85px}
.thumb__label{position:absolute;top:4px;font-family:"Oswald",sans-serif;font-size:7px;color:#fff}
.topic-title{font-size:17.5px}
.topic-copy{width:283px}
</style>
</head>
<body>

<!-- Front sheet -->
<section class="sheet sheet--front">
  <div class="abs brand">
    <div class="brand__name">Vantora</div>
    <div class="brand__sub">Sports Construction</div>
  </div>
  <div class="abs heading tagline">Turnkey Solutions for Sports Construction</div>
  <svg class="abs" style="left:0;top:63px" width="490" height="7"><polygon points="236,0 490,0 490,6 229,6" fill="var(--green)"/></svg>

  <div class="photo hero-front" role="img" aria-label="Aerial view of a track and field under construction with graded sand, equipment and light poles"></div>
  <svg class="abs" style="left:0;top:276px" width="490" height="6"><polygon points="0,0 260,0 266,5 0,5" fill="var(--green)"/></svg>

  <h2 class="abs heading services-title">Services</h2>
  <div class="rule" style="left:0;top:336px;width:75px"></div>
  <div class="abs body services-copy">
    <p>Vantora Sports Construction offers turnkey solutions in the realm of general sports construction. We're committed to excellence in all we do, and we seek to develop lasting relationships with our clients. Vantora is not in the business to win a single job and move on. We are working to earn your trust and business as we want you as a customer for life.</p>
    <p>At Vantora we have 7 Proverbs we strive to live by. Our #1 proverb is to "Deliver On Our Promises". That is our promise to you that we will strive to deliver on time with the quality and service you expect and deserve on every job.</p>
  </div>

  <div class="abs include-box">
    <h3 class="heading">Our Services Include:</h3>
    <div class="include-box__rule"></div>
    <ul class="service-list">
      <li><svg viewBox="0 0 7 6"><polyline points="0.5,3 2.6,5 6.5,0.8" fill="none" stroke="#fff" stroke-width="1.2"/></svg>Track Construction</li>
      <li><svg viewBox="0 0 7 6"><polyline points="0.5,3 2.6,5 6.5,0.8" fill="none" stroke="#fff" stroke-width="1.2"/></svg>Natural Grass Fields</li>
      <li><svg viewBox="0 0 7 6"><polyline points="0.5,3 2.6,5 6.5,0.8" fill="none" stroke="#fff" stroke-width="1.2"/></svg>Synthetic Field Construction</li>
      <li><svg viewBox="0 0 7 6"><polyline points="0.5,3 2.6,5 6.5,0.8" fill="none" stroke="#fff" stroke-width="1.2"/></svg>Stadium Construction</li>
      <li><svg viewBox="0 0 7 6"><polyline points="0.5,3 2.6,5 6.5,0.8" fill="none" stroke="#fff" stroke-width="1.2"/></svg>Tennis Court Construction</li>
      <li><svg viewBox="0 0 7 6"><polyline points="0.5,3 2.6,5 6.5,0.8" fill="none" stroke="#fff" stroke-width="1.2"/></svg>Service + Maintenance</li>
      <li><svg viewBox="0 0 7 6"><polyline points="0.5,3 2.6,5 6.5,0.8" fill="none" stroke="#fff" stroke-width="1.2"/></svg>Stadium Lighting</li>
      <li><svg viewBox="0 0 7 6"><polyline points="0.5,3 2.6,5 6.5,0.8" fill="none" stroke="#fff" stroke-width="1.2"/></svg>Surface Maintenance + Repair</li>
    </ul>
  </div>

  <div class="photo gallery" style="left:22px;background:linear-gradient(160deg,#9aa3ad 0%,#3f8a3a 45%,#8b3a33 80%,#6e6e6e 100%)" role="img" aria-label="Finished synthetic football field surrounded by a red running track"></div>
  <div class="photo gallery" style="left:177px;background:linear-gradient(180deg,#4f87cf 0%,#9cc0e6 42%,#6f9a45 60%,#4a7a2e 100%)" role="img" aria-label="Natural grass baseball field under a blue sky"></div>
  <div class="photo gallery" style="left:331px;background:linear-gradient(180deg,#cfd4d8 0%,#4c9c3a 45%,#3d7e2c 100%)" role="img" aria-label="Worker rolling out synthetic turf on a field"></div>
  <div class="abs gallery-caption" style="left:22px">Track Construction</div>
  <div class="abs gallery-caption" style="left:177px">Natural Grass Fields</div>
  <div class="abs gallery-caption" style="left:331px">Synthetic Field Construction</div>

  <footer class="footer">
    <svg width="490" height="32"><rect width="490" height="32" fill="var(--footer-dark)"/><polygon points="0,0 179,0 166,32 0,32" fill="var(--green)"/></svg>
    <div class="footer__web"><i></i>www.vantorasports.com</div>
    <div class="footer__contact">info@vantorasports.com &nbsp;|&nbsp; 418 North Cedar Avenue Lakeview, Texas 75000 &nbsp;|&nbsp; (555) 010 4821</div>
  </footer>
</section>

<!-- Back sheet -->
<section class="sheet sheet--back">
  <div class="photo hero-back" role="img" aria-label="Aerial view of a completed football stadium with green synthetic field and grandstands"></div>
  <svg class="abs" style="left:0;top:204px" width="490" height="5"><polygon points="0,0 238,0 232,5 0,5" fill="var(--green)"/></svg>

  <div class="photo thumb" style="top:226px;background:linear-gradient(180deg,#8fb3cc 0%,#3f6e37 30%,#7ea652 60%,#5f8b3a 100%)" role="img" aria-label="Aerial view of newly built natural grass fields"></div>
  <div class="photo thumb" style="top:318px;background:linear-gradient(150deg,#b0653a 0%,#c98a5a 50%,#9c5430 100%)" role="img" aria-label="Earth moving equipment grading red dirt for a stadium site"></div>
  <div class="photo thumb" style="top:411px;background:linear-gradient(180deg,#b8c3c9 0%,#6f8e4d 35%,#2f6e2c 100%)" role="img" aria-label="Technician inspecting synthetic turf on a field"></div>
  <div class="photo thumb" style="top:506px;background:linear-gradient(90deg,#3c4a36 0%,#6b7d5c 48%,#2c4e2e 52%,#5cae62 100%)" role="img" aria-label="Before and after comparison of stadium field lighting">
    <span class="thumb__label" style="left:17px">BEFORE</span>
    <span class="thumb__label" style="left:100px">AFTER</span>
  </div>

  <h3 class="abs heading topic-title" style="left:179px;top:231px">Natural Grass Fields</h3>
  <div class="rule" style="left:156px;top:250px;width:58px"></div>
  <p class="abs body topic-copy" style="left:179px;top:257px">Our team operates with specialized equipment allowing massive amounts of dirt to be moved and graded when building natural grass fields. Due to the specialists on our team, we can assist in the design build of your water system to ensure your natural grass will hold the test of time after our installation is complete.</p>

  <h3 class="abs heading topic-title" style="left:179px;top:324px">Stadium Construction</h3>
  <div class="rule" style="left:156px;top:343px;width:58px"></div>
  <p class="abs body topic-copy" style="left:179px;top:351px">We are a true turn-key construction company owned and operated by seasoned professionals who care. From ground-up stadium construction to total lifecycle planning, we provide custom construction solutions through all stages of your projects.</p>

  <h3 class="abs heading topic-title" style="left:186px;top:413px">Service + Maintenance</h3>
  <div class="rule" style="left:164px;top:432px;width:58px"></div>
  <p class="abs body topic-copy" style="left:186px;top:440px">We provide maintenance services and support for all sports surfaces, helping you protect your investment and extend the life of your synthetic turf, track or tennis court through education, performance testing, and maintenance services.</p>

  <h3 class="abs heading topic-title" style="left:186px;top:509px">Stadium Lighting</h3>
  <div class="rule" style="left:164px;top:528px;width:58px"></div>
  <p class="abs body topic-copy" style="left:186px;top:536px">Take advantage of the energy efficiency and cost savings by converting to LED lighting. According to the US Department of Energy, light-emitting diodes (LED) are six to seven times more energy efficient than conventional light bulbs and cut energy use by more than 80 percent.</p>

  <footer class="footer">
    <svg width="490" height="32"><rect width="490" height="32" fill="var(--footer-dark)"/><polygon points="0,0 179,0 166,32 0,32" fill="var(--green)"/></svg>
    <div class="footer__web"><i></i>www.vantorasports.com</div>
    <div class="footer__contact">info@vantorasports.com &nbsp;|&nbsp; 418 North Cedar Avenue Lakeview, Texas 75000 &nbsp;|&nbsp; (555) 010 4821</div>
  </footer>
</section>

</body>
</html>
```